Bakery Business Cards

We are in need of business cards for our bakery business--something non-generic that reflects our business and will stand out. We are a wholesale bakery that primarily services in-store bakeries, casinos, schools, distributors, and fund-raising companies. The family business was founded in 1960. (www.marlowsovenworks.com)

```html
<!DOCTYPE html>
<html lang="en">
<head>
<meta charset="utf-8">
<title>Marlow's Ovenworks — Business Card</title>
<link href="https://fonts.googleapis.com/css2?family=Libre+Baskerville:ital,wght@0,400;0,700;1,400&display=swap" rel="stylesheet">
<style>
  :root {
    --backdrop: #d2d2d2;
    --card-blue: #234797;
    --card-ink: #f4efe6;
    --photo-warm: #d4ab7c;
    --photo-pale: #e9ddd0;
    --photo-deep: #b98a5e;
  }
  * { margin: 0; padding: 0; box-sizing: border-box; }
  html, body {
    width: 1200px; height: 1101px; overflow: hidden;
    background: var(--backdrop);
  }
  .canvas { position: relative; width: 1200px; height: 1101px; }
  .card {
    position: absolute; top: 266px; width: 302px; height: 532px;
  }
  .card-front {
    left: 246px;
    background: var(--card-blue);
    color: var(--card-ink);
    font-family: "Libre Baskerville", serif;
    text-align: center;
  }
  .brand {
    position: absolute; top: 98px; left: 0; right: 0;
  }
  .brand-name {
    font-size: 30px; font-weight: 700; line-height: 1.15;
  }
  .brand-since {
    margin-top: 8px; font-size: 13px; font-weight: 700; letter-spacing: 1px;
  }
  .person { position: absolute; top: 254px; left: 0; right: 0; }
  .person-name { font-size: 23px; font-weight: 400; }
  .person-role { margin-top: 4px; font-size: 17px; font-weight: 700; }
  .divider {
    position: absolute; top: 344px; left: 44px; right: 44px;
    display: flex; align-items: center; gap: 8px;
  }
  .divider-line { flex: 1; height: 1px; background: var(--card-ink); }
  .divider svg { width: 20px; height: 20px; display: block; }
  .contact {
    position: absolute; top: 393px; left: 0; right: 0;
    font-style: italic; font-size: 14px; line-height: 24px;
  }
  .card-back {
    left: 642px;
    background: linear-gradient(160deg, var(--photo-warm) 0%, var(--photo-pale) 50%, var(--photo-deep) 100%);
  }
</style>
</head>
<body>
<main class="canvas">
  <section class="card card-front">
    <div class="brand">
      <div class="brand-name">Marlow's<br>Ovenworks</div>
      <div class="brand-since">SINCE 1960</div>
    </div>
    <div class="person">
      <div class="person-name">Daniel Reyes</div>
      <div class="person-role">Manager</div>
    </div>
    <div class="divider">
      <span class="divider-line"></span>
      <svg viewBox="0 0 20 20" aria-label="Phone"><circle cx="10" cy="10" r="10" fill="#f4efe6"/><path d="M7 5.5l1.6 2.4-1 1.2a7 7 0 003.3 3.3l1.2-1 2.4 1.6-.8 1.6c-3.8.4-8.3-4.1-7.9-7.9z" fill="#234797"/></svg>
      <svg viewBox="0 0 20 20" aria-label="Email"><circle cx="10" cy="10" r="10" fill="#f4efe6"/><rect x="5" y="6.5" width="10" height="7" fill="none" stroke="#234797" stroke-width="1.2"/><path d="M5 6.5l5 4 5-4" fill="none" stroke="#234797" stroke-width="1.2"/></svg>
      <svg viewBox="0 0 20 20" aria-label="Website"><circle cx="10" cy="10" r="10" fill="#f4efe6"/><g fill="none" stroke="#234797" stroke-width="1.1"><circle cx="10" cy="10" r="5"/><ellipse cx="10" cy="10" rx="2.2" ry="5"/><path d="M5 10h10M6 7.5h8M6 12.5h8"/></g></svg>
      <span class="divider-line"></span>
    </div>
    <div class="contact">
      <div>(555) 214-0190</div>
      <div>dreyes@marlowsovenworks.com</div>
      <div>www.marlowsovenworks.com</div>
    </div>
  </section>
  <section class="card card-back" role="img" aria-label="Photo placeholder: overhead view of fruit pies and cobblers on a wooden table"></section>
</main>
</body>
</html>
```